Tidal Ledger

Please see attached Word document for requirements. I want the website to be one page.

Coding

Coded - Design and coding required

Number of Pages Required

1 page

Colors
0054AA
0677BA
7BADD7
CADEEF
E8F1F8

```html
<!DOCTYPE html>
<html lang="en">
<head>
<meta charset="utf-8">
<title>Tidal Ledger — Smart Workforce Scheduling</title>
<link href="https://fonts.googleapis.com/css2?family=Manrope:wght@500;600;700;800&family=Inter:wght@400;500;600;700&display=swap" rel="stylesheet">
<style>
:root{
  --blue:#0054AA;
  --blue-2:#0677BA;
  --blue-3:#7BADD7;
  --blue-4:#CADEEF;
  --blue-5:#E8F1F8;
  --bg:#F5F9FD;
  --ink:#0E1420;
  --muted:#7A8494;
  --line:#E3EAF2;
  --white:#fff;
}
*{box-sizing:border-box;margin:0;padding:0}
html,body{width:1200px;height:4580px;overflow:hidden}
body{background:var(--bg);font-family:"Inter",sans-serif;color:var(--ink);position:relative}
.abs{position:absolute}
h1,h2,h3,.display{font-family:"Manrope",sans-serif;font-weight:800;letter-spacing:-.02em}
.hl{background:var(--blue-4);padding:0 4px}
.btn{display:inline-flex;align-items:center;gap:10px;border-radius:30px;font-size:12px;font-weight:500;height:40px;padding:0 24px;white-space:nowrap}
.btn-primary{background:var(--blue);color:#fff}
.btn-outline{border:1.5px solid var(--ink);color:var(--ink)}
.arrow{width:14px;height:10px}
.logo{display:flex;align-items:center;gap:6px;font-family:"Manrope",sans-serif;font-weight:800;font-size:22px;color:#555e6b}
.logo i{width:10px;height:10px;border:2px solid #555e6b;border-radius:50%}
.section-title{position:absolute;left:0;width:1200px;text-align:center;font-size:36px;line-height:1.05}
/* hero */
.hero-shape{position:absolute;left:490px;top:-10px;width:760px;height:560px;background:linear-gradient(150deg,var(--blue) 20%,var(--blue-2));border-radius:0 0 0 340px}
.hero h1{position:absolute;left:71px;top:130px;font-size:48px;line-height:1.1;width:500px}
.hero-sub{position:absolute;left:71px;top:306px;font-size:12px;line-height:1.9;color:#333;width:440px}
.dash{position:absolute;left:600px;top:100px;width:600px;height:440px;background:#fff;border-radius:18px 0 0 18px;box-shadow:0 20px 50px rgba(0,40,90,.12)}
.stat-box{position:absolute;top:136px;width:128px;height:60px;background:#fff;border-radius:10px;box-shadow:0 6px 18px rgba(0,40,90,.08);display:flex;align-items:center;gap:10px;padding-left:14px}
.stat-box b{font-family:"Manrope",sans-serif;font-size:20px;display:block}
.stat-box small{font-size:7px;color:var(--muted);letter-spacing:.05em}
.trow{position:absolute;left:108px;width:480px;display:flex;font-size:7px;color:#555}
.trow span{flex:1}
.pop{position:absolute;background:#fff;border-radius:14px;box-shadow:0 10px 30px rgba(0,40,90,.14)}
/* logos */
.pill{position:absolute;height:80px;background:#fff;border-radius:40px;box-shadow:0 8px 24px rgba(0,40,90,.06);display:flex;align-items:center;justify-content:center;gap:8px;font-family:"Manrope",sans-serif;font-weight:800;font-size:24px;color:#111;white-space:nowrap}
.pill i{width:18px;height:18px;border-radius:50%;background:#111;flex:none}
/* why */
.why-item{position:absolute;left:71px;width:427px;height:90px;padding:22px 20px 0 68px;border-bottom:1px solid var(--line)}
.why-item.active{background:#fff;border-radius:10px;border:none;box-shadow:0 8px 24px rgba(0,40,90,.07)}
.why-item .ic{position:absolute;left:18px;top:28px;width:34px;height:34px;border-radius:50%}
.why-item h3{font-size:16px;margin-bottom:8px}
.why-item p{font-size:12px;color:var(--muted)}
/* stats */
.stats{position:absolute;left:71px;top:1586px;width:1058px;height:130px;background:var(--blue);border-radius:10px;display:flex;align-items:center;color:#fff;box-shadow:0 14px 30px rgba(0,84,170,.25)}
.stats div{flex:1;text-align:center}
.stats b{display:block;font-family:"Manrope",sans-serif;font-weight:800;font-size:34px}
.stats span{font-size:11px}
/* features */
.feat{position:absolute;width:342px;height:208px;background:#fff;border-radius:12px;box-shadow:0 8px 26px rgba(0,40,90,.06);text-align:center;padding-top:40px}
.feat .ic{width:36px;height:36px;border-radius:50%;margin:0 auto 20px}
.feat h3{font-size:16px;margin-bottom:8px}
.feat p{font-size:16px;color:var(--muted);line-height:1.3;width:260px;margin:0 auto}
/* testimonials */
.tcard{position:absolute;text-align:center}
.tcard .face{border-radius:50%;margin:0 auto}
.tcard h4{font-family:"Manrope",sans-serif;font-weight:800;font-size:16px;margin-top:10px}
.tcard small{font-size:12px;display:block;margin:4px 0 16px}
.tcard p{font-size:16px;line-height:1.25;color:#555}
.faded{opacity:.35}
.faded h4{font-size:14px}
.faded small{font-size:10px;margin-bottom:12px}
.faded p{font-size:13px}
.tcard-main{position:absolute;left:354px;top:2648px;width:492px;height:182px;background:#fff;border-radius:0 0 14px 14px}
/* industries */
.ind{position:absolute;top:2987px;width:140px;height:116px;background:#fff;border-radius:10px;box-shadow:0 8px 22px rgba(0,40,90,.06);text-align:center;padding-top:28px;font-family:"Manrope",sans-serif;font-weight:700;font-size:12px}
.ind i{display:block;width:32px;height:32px;border-radius:50%;margin:0 auto 14px}
/* pricing */
.plan{position:absolute;top:3245px;width:342px;height:435px;background:#fff;border-radius:12px;box-shadow:0 8px 26px rgba(0,40,90,.06);padding:32px 32px}
.plan h3{font-size:18px}
.plan .d{font-size:15px;color:var(--muted);line-height:1.3;margin:10px 0 14px}
.plan .price{font-family:"Manrope",sans-serif;font-weight:800;font-size:28px}
.plan .price small{font-family:"Inter",sans-serif;font-weight:400;font-size:14px;color:var(--muted)}
.plan ul{list-style:none;background:#F6F9FC;border:1px solid var(--line);border-radius:10px;margin-top:18px;height:180px;padding:14px 12px}
.plan li{display:flex;align-items:center;gap:10px;font-size:14px;color:#444;height:31px}
.plan li i{width:16px;height:16px;border-radius:50%;background:var(--blue);flex:none}
.plan .btn{position:absolute;left:32px;bottom:32px;width:278px;justify-content:center}
/* cta */
.cta{position:absolute;left:135px;top:3773px;width:928px;height:481px;border-radius:40px;background:linear-gradient(180deg,var(--blue) 0%,var(--blue-2) 100%);text-align:center;color:#fff}
.cta h2{font-size:40px;line-height:1.25;margin-top:22px}
.cta .btn{height:38px}
/* footer */
.foot{position:absolute;font-size:11px;color:#555;line-height:2.7}
.foot h5{font-size:12px;font-weight:600;color:var(--ink);line-height:1}
.soc{width:30px;height:30px;border-radius:50%;background:var(--blue);display:inline-block;margin-left:10px}
</style>
</head>
<body>

<!-- HERO -->
<header class="hero">
  <div class="hero-shape"></div>
  <div class="abs logo" style="left:70px;top:30px"><i></i>tidal ledger</div>
  <a class="abs btn" style="left:1008px;top:25px;background:#fff;color:var(--blue);height:41px;padding:0 22px;font-size:12px">Start Free Trial</a>
  <h1>Smart Workforce <span class="hl">Scheduling</span> Made Simple</h1>
  <p class="hero-sub">Automate Your Staff Rosters, Reduce Costs, And Manage Teams Efficiently With An Intelligent Scheduling Platform Built For Modern Businesses.</p>
  <a class="abs btn btn-primary" style="left:71px;top:373px">Start Free Trial <svg class="arrow" viewBox="0 0 14 10"><path d="M0 5h12M8 1l4 4-4 4" stroke="#fff" stroke-width="1.6" fill="none"/></svg></a>
  <a class="abs btn btn-outline" style="left:243px;top:373px">Book a Demo <svg class="arrow" viewBox="0 0 14 10"><path d="M0 5h12M8 1l4 4-4 4" stroke="#111" stroke-width="1.6" fill="none"/></svg></a>
  <p class="abs" style="left:71px;top:488px;font-size:14px">Join Thousands Of Teams Already Using <b style="color:var(--blue)">Tidal Ledger</b></p>
  <div class="abs" role="img" aria-label="Customer portrait avatars" style="left:71px;top:534px;width:100px;height:44px">
    <span class="abs" style="left:0;width:42px;height:42px;border-radius:50%;background:#8a6a55;border:2px solid #fff"></span>
    <span class="abs" style="left:28px;width:42px;height:42px;border-radius:50%;background:#3e4a5c;border:2px solid #fff"></span>
    <span class="abs" style="left:56px;width:42px;height:42px;border-radius:50%;background:#c9a27e;border:2px solid #fff"></span>
  </div>
  <div class="abs" style="left:188px;top:532px"><b class="display" style="font-size:22px">2,291</b><br><span style="font-size:11px;color:var(--muted)">Happy Customers</span></div>
  <div class="abs" style="left:305px;top:534px;width:1px;height:44px;background:var(--line)"></div>
  <div class="abs" style="left:322px;top:532px"><b class="display" style="font-size:22px">4.8/5</b><br><span style="font-size:11px;color:var(--blue)">★★★★</span><span style="font-size:11px;color:var(--muted)"> Rating</span></div>

  <!-- dashboard -->
  <svg class="abs" style="left:912px;top:470px" width="210" height="120" viewBox="0 0 210 120"><path d="M0 0h210a105 105 0 0 1-210 0z" fill="var(--blue-3)"/></svg>
  <div class="dash">
    <svg class="abs" style="left:34px;top:46px" width="14" height="300"><rect x="2" y="2" width="10" height="8" rx="2" fill="#aab"/><circle cx="7" cy="32" r="4" fill="#aab"/><rect x="3" y="280" width="8" height="8" rx="2" fill="#aab"/></svg>
    <h3 class="abs" style="left:88px;top:52px;font-size:24px;font-weight:700;color:#2a3140">Dashboard</h3>
    <div class="abs" style="left:93px;top:104px;font-size:8px;color:#999;display:flex;gap:32px"><span style="color:#111;border-bottom:2px solid var(--blue)">All</span><span>Live</span><span>Recent</span><span>History</span></div>
    <div class="stat-box" style="left:92px"><svg width="28" height="28"><circle cx="14" cy="14" r="11" stroke="#e8eef5" stroke-width="4" fill="none"/><path d="M14 3a11 11 0 1 1-11 11" stroke="#22b573" stroke-width="4" fill="none"/></svg><div><b>2034</b><small>COMPLETED</small></div></div>
    <div class="stat-box" style="left:234px"><svg width="28" height="28"><circle cx="14" cy="14" r="11" stroke="#e8eef5" stroke-width="4" fill="none"/><path d="M3 14a11 11 0 0 1 11-11" stroke="var(--blue)" stroke-width="4" fill="none"/></svg><div><b>234</b><small>COMPLETED</small></div></div>
    <div class="stat-box" style="left:376px"><svg width="28" height="28"><circle cx="14" cy="14" r="11" stroke="#e8eef5" stroke-width="4" fill="none"/><path d="M3 14a11 11 0 0 1 6-9.8" stroke="var(--blue-2)" stroke-width="4" fill="none"/></svg><div><b>3420</b><small>COMPLETED</small></div></div>
    <div class="stat-box" style="left:518px"><svg width="28" height="28"><circle cx="14" cy="14" r="11" stroke="#e8eef5" stroke-width="4" fill="none"/><path d="M14 3a11 11 0 0 1 8 3.5" stroke="#f5a623" stroke-width="4" fill="none"/></svg><div><b>2</b><small>COMPLETED</small></div></div>
    <div class="trow" style="top:256px"><span><b>Lena Harlow</b></span><span>221</span><span>100.0%</span><span>12.0%</span><span>8.0%</span><span>73.2%</span></div>
    <div class="trow" style="top:296px"><span><b>Theo Marsh</b></span><span>43</span><span>41.0%</span><span>80%</span><span>18.0%</span><span>73.2</span></div>
    <div class="trow" style="top:336px"><span></span><span></span><span>53.0%</span><span>42.9%</span><span>4.0%</span><span>73.2%</span></div>
    <div class="trow" style="top:376px"><span></span><span></span><span>100.0%</span><span>82.9%</span><span>8.0%</span><span>73.2%</span></div>
  </div>
  <div class="pop" style="left:918px;top:98px;width:172px;height:144px;text-align:center;padding-top:20px">
    <svg width="20" height="20"><circle cx="10" cy="6" r="4" fill="#22b573"/><path d="M2 19a8 8 0 0 1 16 0z" fill="#22b573"/></svg>
    <div class="display" style="font-size:18px;font-weight:700">32000+</div>
    <div style="font-size:9px;color:var(--muted)">Customers</div>
    <svg width="140" height="34"><path d="M4 24c16-26 30 10 46-6s28-20 44 0 30 14 42-6" stroke="var(--blue)" stroke-width="3" fill="none"/></svg>
  </div>
  <div class="abs" style="left:1104px;top:168px;font-size:10px;white-space:nowrap"><b>Rina Okafor</b><br><span style="font-size:8px;color:var(--muted)">Developer</span></div>
  <div class="pop" style="left:660px;top:420px;width:204px;height:186px">
    <div class="abs" style="left:32px;top:14px;font-size:9px;font-weight:600">Based Social</div>
    <svg class="abs" style="left:56px;top:40px" width="92" height="92"><circle cx="46" cy="46" r="30" stroke="var(--blue-4)" stroke-width="16" fill="none"/><path d="M46 16a30 30 0 1 1-30 30" stroke="var(--blue)" stroke-width="16" fill="none"/></svg>
    <div class="abs" style="left:32px;top:146px;width:142px;height:5px;border-radius:3px;background:var(--blue-3)"></div>
    <div class="abs" style="left:80px;top:142px;width:14px;height:14px;border-radius:50%;background:#fff;border:3px solid var(--blue)"></div>
  </div>
  <div class="abs" style="left:906px;top:575px;width:10px;height:10px;border-radius:50%;background:var(--blue)"></div>
</header>

<!-- TRUST -->
<p class="abs" style="left:0;width:1200px;top:690px;text-align:center;font-size:11px">Trusted By 20,000+ Teams <span style="color:var(--blue)">★★★★</span></p>
<h2 class="section-title" style="top:718px">They <span class="hl">Trust</span> Us.</h2>
<div class="pill" style="left:40px;top:782px;width:180px"><i></i>Lumora</div>
<div class="pill" style="left:238px;top:782px;width:124px">Vantly</div>
<div class="pill" style="left:380px;top:782px;width:180px"><i style="background:#2bb24c;border-radius:3px"></i>Orbita</div>
<div class="pill" style="left:578px;top:782px;width:210px"><i style="background:#6d4ad8;border-radius:3px"></i>Kestrel</div>
<div class="pill" style="left:808px;top:782px;width:180px;font-size:16px"><i style="width:12px;height:12px;background:var(--blue)"></i>PENMARQ</div>
<div class="pill" style="left:1006px;top:782px;width:180px;font-size:16px"><i style="background:#15b374"></i>Quillon</div>
<div class="pill" style="left:-40px;top:884px;width:132px;justify-content:flex-end;padding-right:18px;font-size:22px">Tessary</div>
<div class="pill" style="left:112px;top:884px;width:180px">Peoplix</div>
<div class="pill" style="left:310px;top:884px;width:180px;font-size:20px"><i style="background:#ff5100;border-radius:4px"></i>Chatterly</div>
<div class="pill" style="left:510px;top:884px;width:180px"><i style="background:#fdb300"></i>Facet</div>
<div class="pill" style="left:710px;top:884px;width:180px"><i></i>Terrane</div>
<div class="pill" style="left:908px;top:884px;width:180px;font-size:14px"><i style="background:#e2761b;border-radius:3px"></i>VAULTRY</div>
<div class="pill" style="left:1106px;top:884px;width:140px;justify-content:flex-start;padding-left:34px"><i style="background:#ec2059"></i>Pivra</div>

<!-- WHY -->
<h2 class="section-title" style="top:1050px">Why <span class="hl">Choose</span> Tidal Ledger</h2>
<div class="why-item active" style="top:1104px"><span class="ic" style="background:#fde7ea"></span><h3>Automated Scheduling</h3><p>Create staff schedules instantly with smart automation</p></div>
<div class="why-item" style="top:1204px"><span class="ic" style="background:#e3f5e8"></span><h3>Cost Reduction</h3><p>Reduce overtime and control staffing costs easil</p></div>
<div class="why-item" style="top:1304px"><span class="ic" style="background:#e3eefa"></span><h3>Fair Shift Allocation</h3><p>Ensure balanced and fair shifts for all employees</p></div>
<div class="why-item" style="top:1404px"><span class="ic" style="background:#e8edf3"></span><h3>Multi-Industry Ready</h3><p>Works across healthcare, retail, logistics and more</p></div>

<div class="abs" style="left:655px;top:1160px;width:400px;height:275px;background:#EDF3FA;border-radius:12px"></div>
<svg class="abs" style="left:740px;top:1240px" width="320" height="150" viewBox="0 0 320 150"><defs><linearGradient id="ar" x1="0" y1="0" x2="0" y2="1"><stop offset="0" stop-color="#7BADD7" stop-opacity=".4"/><stop offset="1" stop-color="#7BADD7" stop-opacity="0"/></linearGradient></defs><path d="M0 120c40 0 50-30 70 10s40 20 60-30 40-40 60-10 40 20 70-50 40-90 40-90v150H0z" fill="url(#ar)"/><path d="M0 120c40 0 50-30 70 10s40 20 60-30 40-40 60-10 40 20 70-50 40-90 40-90" stroke="var(--blue)" stroke-width="3" fill="none"/><circle cx="226" cy="70" r="7" fill="#fff" stroke="var(--blue)" stroke-width="3"/></svg>
<div class="abs display" style="left:904px;top:1242px;font-size:15px;font-weight:700;text-align:center">5,560$<br><span style="font-size:10px;font-weight:500">Ratings</span></div>
<div class="abs btn btn-primary" style="left:953px;top:1170px;height:30px;font-size:13px;padding:0 24px">Monthly</div>
<div class="pop" style="left:563px;top:1170px;width:260px;height:203px">
  <div class="abs" style="left:34px;top:34px;font-size:13px;font-weight:600">Users Activity</div>
  <div class="abs" style="left:168px;top:30px;font-size:10px;color:var(--muted)">This Week ⌄</div>
  <svg class="abs" style="left:30px;top:62px" width="210" height="120"><g font-size="7" fill="#999"><text x="0" y="8">300</text><text x="0" y="38">200</text><text x="0" y="68">100</text><text x="0" y="98">0</text></g><g fill="var(--blue)"><rect x="38" y="30" width="5" height="66"/><rect x="46" y="56" width="5" height="40"/><rect x="62" y="40" width="5" height="56"/><rect x="70" y="60" width="5" height="36"/><rect x="86" y="22" width="5" height="74"/><rect x="94" y="50" width="5" height="46"/><rect x="110" y="36" width="5" height="60"/><rect x="118" y="58" width="5" height="38"/><rect x="134" y="28" width="5" height="68"/><rect x="142" y="54" width="5" height="42"/><rect x="158" y="18" width="5" height="78"/><rect x="166" y="60" width="5" height="36"/></g><g font-size="7" fill="#999"><text x="40" y="110">M</text><text x="64" y="110">T</text><text x="88" y="110">W</text><text x="112" y="110">T</text><text x="136" y="110">F</text><text x="160" y="110">S</text><text x="182" y="110">S</text></g></svg>
</div>
<div class="pop" style="left:900px;top:1382px;width:258px;height:92px">
  <span class="abs" style="left:22px;top:28px;width:34px;height:34px;border-radius:50%;background:var(--blue-5)"></span>
  <div class="abs display" style="left:78px;top:24px;font-size:18px;font-weight:700">$4,250</div>
  <div class="abs" style="left:78px;top:56px;font-size:11px;color:var(--muted)">Earned this month</div>
</div>

<!-- STATS -->
<div class="stats">
  <div><b>110+</b><span>Businesses Using Tidal Ledger</span></div>
  <div><b>4M+</b><span>Shifts Scheduled Automatically</span></div>
  <div><b>99.9%</b><span>Accuracy In Scheduling</span></div>
  <div><b>50+</b><span>Industries Supported Worldwide</span></div>
</div>

<!-- FEATURES -->
<h2 class="section-title" style="top:1808px">Powerful <span class="hl">Features</span> Built For<br>Modern Teams</h2>
<div class="feat" style="left:71px;top:1908px"><div class="ic" style="background:#fde4ec"></div><h3>Smart Scheduling Engine</h3><p>Automatically creates optimised staff schedules</p></div>
<div class="feat" style="left:428px;top:1908px"><div class="ic" style="background:#fde6e3"></div><h3>Compliance Management</h3><p>Ensure labor rules and policies are followed</p></div>
<div class="feat" style="left:786px;top:1908px"><div class="ic" style="background:#e3eefa"></div><h3>Cost Control Tools</h3><p>Track and reduce workforce expenses</p></div>
<div class="feat" style="left:71px;top:2135px"><div class="ic" style="background:#fdeee0"></div><h3>Multi-Location Management</h3><p>Manage multiple sites from one place</p></div>
<div class="feat" style="left:428px;top:2135px"><div class="ic" style="background:#efe6fb"></div><h3>Employee Self-Service</h3><p>Staff can manage shifts and requests easily</p></div>
<div class="feat" style="left:786px;top:2135px"><div class="ic" style="background:#e3eefa"></div><h3>Live Updates &amp; Alerts</h3><p>Get instant notifications for any changes</p></div>

<!-- TESTIMONIALS -->
<h2 class="section-title" style="top:2435px">Trusted By <span class="hl">Growing</span> Teams</h2>
<svg class="abs" style="left:320px;top:2500px" width="560" height="70"><path d="M0 10Q280 90 560 10" stroke="#c9d3de" stroke-width="1.5" fill="none"/><circle cx="280" cy="50" r="12" fill="var(--blue)"/></svg>
<div class="tcard faded" style="left:166px;top:2522px;width:360px"><div class="face" role="img" aria-label="Customer portrait" style="width:38px;height:38px;background:#c8ccd2"></div><h4>Clara Venhollow</h4><small>Operations Manager</small><p>“Tidal Ledger has completely transformed our scheduling process. What used to take hours is now done in minutes.”</p></div>
<div class="tcard faded" style="left:676px;top:2522px;width:360px"><div class="face" role="img" aria-label="Customer portrait" style="width:38px;height:38px;background:#c8ccd2"></div><h4>Clara Venhollow</h4><small>Operations Manager</small><p>“Tidal Ledger has completely transformed our scheduling process. What used to take hours is now done in minutes.”</p></div>
<div class="tcard-main"></div>
<div class="tcard" style="left:390px;top:2600px;width:420px"><div class="face" role="img" aria-label="Customer portrait" style="width:80px;height:80px;background:linear-gradient(#5a4a40,#2c2420)"></div><h4>Clara Venhollow</h4><small>Operations Manager</small><p>“Tidal Ledger has completely transformed our scheduling process. What used to take hours is now done in minutes.”</p></div>

<!-- INDUSTRIES -->
<h2 class="section-title" style="top:2923px">Built For <span class="hl">Every</span> Industry</h2>
<div class="ind" style="left:71px"><i style="background:#fde4ec"></i>Healthcare</div>
<div class="ind" style="left:224px"><i style="background:#fde6e3"></i>Retail</div>
<div class="ind" style="left:376px"><i style="background:#e3eefa"></i>Hospitality</div>
<div class="ind" style="left:529px"><i style="background:#fdeee0"></i>Logistics</div>
<div class="ind" style="left:682px"><i style="background:#efe6fb"></i>Manufacturing</div>
<div class="ind" style="left:835px"><i style="background:#e3eefa"></i>Security</div>
<div class="ind" style="left:988px"><i style="background:#e3eefa"></i>Events</div>

<!-- PRICING -->
<h2 class="section-title" style="top:3191px">Simple <span class="hl">Pricing</span> Plans</h2>
<div class="plan" style="left:71px"><h3>Starter Plan</h3><p class="d">Perfect for larger organizations with advanced needs</p><div class="price">$0<small> / per month</small></div>
<ul><li><i></i>Staff scheduling tools</li><li><i></i>Shift management</li><li><i></i>Basic automation</li><li><i></i>Email support</li></ul>
<a class="btn btn-primary">Select This Plan <svg class="arrow" viewBox="0 0 14 10"><path d="M0 5h12M8 1l4 4-4 4" stroke="#fff" stroke-width="1.6" fill="none"/></svg></a></div>
<div class="plan" style="left:428px"><h3>Professional</h3><p class="d">Perfect for larger organizations with advanced needs</p><div class="price">$49<small> / per month</small></div>
<ul><li><i></i>Smart scheduling automation</li><li><i></i>Compliance management</li><li><i></i>Multi-location support</li><li><i></i>Real-time updates</li><li><i></i>Priority support</li></ul>
<a class="btn btn-primary">Select This Plan <svg class="arrow" viewBox="0 0 14 10"><path d="M0 5h12M8 1l4 4-4 4" stroke="#fff" stroke-width="1.6" fill="none"/></svg></a></div>
<div class="plan" style="left:786px"><h3>Enterprise</h3><p class="d">Perfect for larger organizations with advanced needs</p><div class="price">$99<small> / per month</small></div>
<ul><li><i></i>Full automation suite</li><li><i></i>Advanced analytics &amp; insights</li><li><i></i>Custom integrations</li><li><i></i>Dedicated support</li><li><i></i>Enterprise-grade security</li></ul>
<a class="btn btn-primary">Select This Plan <svg class="arrow" viewBox="0 0 14 10"><path d="M0 5h12M8 1l4 4-4 4" stroke="#fff" stroke-width="1.6" fill="none"/></svg></a></div>

<!-- CTA -->
<section class="cta">
  <p style="margin-top:98px;font-size:11px"><span style="color:#f5c518">★★★★★</span> 4.9/5</p>
  <div role="img" aria-label="Customer avatars" style="margin:10px auto 0;width:140px;height:30px;display:flex;justify-content:center">
    <span style="width:30px;height:30px;border-radius:50%;background:#b8c4d2;border:2px solid #fff"></span>
    <span style="width:30px;height:30px;border-radius:50%;background:#8d9bb0;border:2px solid #fff;margin-left:-6px"></span>
    <span style="width:30px;height:30px;border-radius:50%;background:#a9b6c6;border:2px solid #fff;margin-left:-6px"></span>
    <span style="width:30px;height:30px;border-radius:50%;background:#7f8ea4;border:2px solid #fff;margin-left:-6px"></span>
    <span style="width:30px;height:30px;border-radius:50%;background:#fff;color:var(--blue);font-size:7px;line-height:26px;margin-left:-6px">100K+</span>
  </div>
  <p style="font-size:12px;line-height:1.6;margin-top:10px">Over 100K+ Entrepreneurs, and<br>business choose us</p>
  <h2>Ready To Transform Your<br>Workforce?</h2>
  <p style="font-size:16px;margin-top:14px;color:#dfe9f5">Start automating your scheduling and improve team efficiency today.</p>
  <div style="margin-top:26px;display:flex;gap:16px;justify-content:center">
    <a class="btn" style="background:#fff;color:var(--ink)">Start Free Trial <svg class="arrow" viewBox="0 0 14 10"><path d="M0 5h12M8 1l4 4-4 4" stroke="#111" stroke-width="1.6" fill="none"/></svg></a>
    <a class="btn" style="border:1.5px solid #fff;color:#fff">Book a Demo <svg class="arrow" viewBox="0 0 14 10"><path d="M0 5h12M8 1l4 4-4 4" stroke="#fff" stroke-width="1.6" fill="none"/></svg></a>
  </div>
</section>

<!-- FOOTER -->
<footer>
  <div class="abs logo" style="left:70px;top:4325px"><i></i>tidal ledger</div>
  <p class="foot" style="left:71px;top:4370px;width:220px;line-height:1.45">Tidal Ledger is an intelligent workforce scheduling platform that helps businesses automate staff rosters, reduce costs, and manage teams efficiently across multiple industries.</p>
  <div class="foot" style="left:359px;top:4332px"><h5>Quick Links</h5>Features<br>Pricing<br>Contact</div>
  <div class="foot" style="left:525px;top:4332px"><h5>Contact Info</h5>Phone: (00) 555 018 224<br>Email: hello@tidalledger.example</div>
  <div class="foot" style="left:753px;top:4332px"><h5>Subscribe</h5>Join our newsletter to stay up to date on features and releases.</div>
  <div class="abs" style="left:753px;top:4398px;width:376px;height:50px;border:1px solid var(--line);border-radius:25px;background:#fff">
    <span class="abs" style="left:20px;top:18px;width:16px;height:12px;border:1.5px solid #999;border-radius:2px"></span>
    <span class="abs" style="left:48px;top:17px;font-size:11px;color:#999">Enter your email</span>
    <a class="abs btn btn-primary" style="right:6px;top:5px;height:38px">Subscribe <svg class="arrow" viewBox="0 0 14 10"><path d="M0 5h12M8 1l4 4-4 4" stroke="#fff" stroke-width="1.6" fill="none"/></svg></a>
  </div>
  <p class="abs" style="left:753px;top:4460px;font-size:8px;color:#555">By subscribing you agree to with our <u>Privacy Policy</u></p>
  <div class="abs" style="left:71px;top:4510px;width:1058px;height:1px;background:var(--line)"></div>
  <p class="abs" style="left:71px;top:4536px;font-size:11px;color:#555">© 2026 Tidal Ledger. All rights reserved.</p>
  <div class="abs" style="left:964px;top:4528px"><span class="soc"></span><span class="soc"></span><span class="soc"></span><span class="soc"></span></div>
</footer>
</body>
</html>
```